Upbeat Accouting Package Flyer

I am looking for a 1 page (front, or front and back) flyer that will become our marketing for our accounting services. We are looking for something a little different and we are catering to the small retail shop owners. We have 3 accounting packages we would like to display and then some add-ons. I have included our logo that must be included in the design. I have uploaded the accounting package information as well.
Target Market(s)
Small Retail Shop Owners
Industry/Entity Type
Accounting
Colors
Designer to choose colors to be used in the design.
Requirements
Must have
- A casual feel. We are not your typical accountants who are very professional and "stuffy". I want it to feel like we are all family.
Nice to have
- I would like to incorporate some sort of retail theme.
- We have a couple of taglines we like to use and it would be great if they could be included. They are "We know you CAN do the accounting, but do you WANT to?" and "We allow you to get back to what's important."
Should not have
- Typical stock accounting photos of people shaking hands, large office buildings, etc.

```html
<!DOCTYPE html>
<html lang="en">
<head>
<meta charset="utf-8">
<title>Accounting Packages Flyer</title>
<link href="https://fonts.googleapis.com/css2?family=Montserrat:wght@400;500;700;800&display=swap" rel="stylesheet">
<style>
  :root {
    --cyan: #1ab4d2;
    --ink: #1f1f1f;
    --text: #2b2b2b;
    --rule: #cfcfcf;
    --band-grey: #5e5e5e;
    --backdrop: #ececec;
    --paper: #ffffff;
  }
  * { box-sizing: border-box; margin: 0; padding: 0; }
  html, body { width: 1200px; height: 1200px; overflow: hidden; }
  body {
    background: var(--backdrop);
    font-family: "Montserrat", Arial, sans-serif;
    color: var(--text);
    display: flex; justify-content: center; align-items: center;
  }
  .flyer {
    width: 848px; height: 1200px;
    background: var(--paper);
    position: relative;
    padding: 54px 0 0;
  }
  .flyer-title {
    text-align: center;
    font-weight: 800;
    font-size: 44px;
    color: var(--ink);
    letter-spacing: -0.5px;
    margin-bottom: 30px;
  }
  .package {
    width: 660px;
    border: 1.5px solid var(--rule);
    border-radius: 10px;
    overflow: hidden;
    margin-bottom: 24px;
  }
  .package--develop { margin-left: 34px; }
  .package--grow { margin-left: 72px; }
  .package--relax { margin-left: 110px; }
  .package--extras { margin-left: 148px; }
  .package-band {
    background: var(--cyan);
    color: #fff;
    font-weight: 700;
    font-size: 16px;
    text-align: center;
    padding: 6px 0;
    letter-spacing: 0.3px;
  }
  .package-body {
    display: grid;
    grid-template-columns: 1fr 1fr;
    gap: 0 22px;
    padding: 14px 22px 16px;
  }
  .checklist { list-style: none; }
  .checklist li {
    position: relative;
    padding-left: 24px;
    font-size: 14px;
    line-height: 1.3;
    margin-bottom: 6px;
  }
  .checklist li::before {
    content: "";
    position: absolute; left: 0; top: 3px;
    width: 11px; height: 11px;
    border: 1.5px solid var(--cyan);
    border-radius: 2px;
  }
  .checklist li::after {
    content: "";
    position: absolute; left: 4px; top: 4px;
    width: 4px; height: 7px;
    border-right: 2px solid var(--cyan);
    border-bottom: 2px solid var(--cyan);
    transform: rotate(40deg);
  }
  .flyer-footer {
    position: absolute;
    left: 0; right: 0; bottom: 70px;
    height: 96px;
    display: flex; align-items: center;
  }
  .brand {
    padding-left: 70px;
    width: 360px;
    font-weight: 800;
    font-size: 30px;
    line-height: 1.05;
    color: var(--ink);
  }
  .web-band {
    flex: 1;
    height: 44px;
    background: var(--band-grey);
    color: #fff;
    font-size: 17px;
    letter-spacing: 3px;
    display: flex; align-items: center; justify-content: center;
    align-self: flex-start;
    margin-top: 6px;
  }
</style>
</head>
<body>
  <main class="flyer">
    <h1 class="flyer-title">Accounting Packages:</h1>

    <section class="package package--develop">
      <div class="package-band">DEVELOP :</div>
      <div class="package-body">
        <ul class="checklist">
          <li>$300/mo when paid annually $325/mo billed monthly</li>
          <li>BrightBooks Online subscription</li>
          <li>Free accounting setup</li>
        </ul>
        <ul class="checklist">
          <li>Weekly transaction processing</li>
          <li>Monthly account reconciliation (up to 2 accounts)</li>
          <li>Monthly financial statements by the 15th of the month</li>
        </ul>
      </div>
    </section>

    <section class="package package--grow">
      <div class="package-band">GROW :</div>
      <div class="package-body">
        <ul class="checklist">
          <li>$550/mo billed annually, $575/mo billed monthly</li>
          <li>BrightBooks Online subscription</li>
          <li>Free accounting setup</li>
          <li>Weekly transaction processing</li>
          <li>Monthly account reconciliation (up to 4 accounts)</li>
        </ul>
        <ul class="checklist">
          <li>Monthly financial statements by the 10th of the month</li>
          <li>Client portal access for document sharing</li>
          <li>1 Custom Report</li>
          <li>Accounts Payable</li>
          <li>Monthly Scorecard (customized metric tracking for your business)</li>
        </ul>
      </div>
    </section>

    <section class="package package--relax">
      <div class="package-band">RELAX (WE'VE GOT THIS):</div>
      <div class="package-body">
        <ul class="checklist">
          <li>$850/mo billed annually, $875/mo billed monthly</li>
          <li>BrightBooks Online subscription</li>
          <li>Free accounting setup</li>
          <li>Weekly transaction processing</li>
          <li>Monthly account reconciliation (up to 5-10 accounts)</li>
          <li>Monthly financial statements by the 5th of the month</li>
        </ul>
        <ul class="checklist">
          <li>Client portal access for document sharing</li>
          <li>2 Custom Reports</li>
          <li>Accounts Payable</li>
          <li>Invoicing and accounts receivable</li>
          <li>Weekly Scorecard (customized metric tracking for your business)</li>
        </ul>
      </div>
    </section>

    <section class="package package--extras">
      <div class="package-band">ADDITIONAL OPTIONS</div>
      <div class="package-body">
        <ul class="checklist">
          <li>Payroll - 1-10 employees $85/mo; 11-30 employees $175/mo</li>
          <li>Sales tax - $30/mo per state</li>
        </ul>
        <ul class="checklist">
          <li>Corporate taxes $50/mo</li>
          <li>Owner taxes - $25/mo</li>
        </ul>
      </div>
    </section>

    <footer class="flyer-footer">
      <div class="brand">Keystone Ledger<br>&amp; Tax Co.</div>
      <div class="web-band">www.keystoneledger.com</div>
    </footer>
  </main>
</body>
</html>
```